Commercial Bakery needs packing design for a Bread Bag.

Dorne's Bakery needs a design for a bread bag to be distributed to grocery stores. We make all kinds of breads and want this packaging to represent our company. We would like the packaging to be black and white with a fun/bubbly modern design. I have attached a few ideas of what I am looking for.
There are 5 different products. Packaging must be the same for each product except for corresponding product name, bar code and nutrional facts.
Product names:
Coconut Cream Bread
Cream Bread
Potato Rolls
Roll ups
Coconut & Raisin Bread

Our products are packaged in a 11” x 8” poly bag.
I will open 5 contracts with whoever’s design I select. I will then provide nutritional facts, barcodes for items once a contract is selected. Thank you!!

Target Market(s)

Grocery stores

Industry/Entity Type

Bakery

Requirements
Must have
• Black and White (off whites are ok)
Should not have
• Color

```html
<!DOCTYPE html>
<html lang="en">
<head>
<meta charset="utf-8">
<title>Dorne's Bakery – Bread Bag</title>
<link rel="stylesheet" href="https://fonts.googleapis.com/css2?family=Montserrat:wght@400;500&family=Cabin:wght@400&display=swap">
<style>
  :root {
    --page: #e2b088;
    --bag: #e9c19f;
    --crust-light: #d9b48f;
    --crust-mid: #b98a60;
    --crust-dark: #8a5a36;
    --paper: #ffffff;
    --ink: #111111;
  }
  html, body {
    margin: 0;
    width: 1200px;
    height: 1200px;
    overflow: hidden;
    background: var(--page);
  }
  .bag-front {
    position: absolute;
    left: 230px;
    top: 55px;
    width: 740px;
    height: 1090px;
    background: var(--bag);
    overflow: hidden;
  }
  .loaf-photo {
    position: absolute;
    left: 117px;
    top: 159px;
    width: 532px;
    height: 900px;
  }
  .wheat-pattern {
    position: absolute;
    left: 0;
    top: 0;
    width: 740px;
    height: 1090px;
    background: linear-gradient(180deg, rgba(17,17,17,0) 0%, rgba(17,17,17,0) 40%, rgba(17,17,17,0.05) 100%);
  }
  .label-band {
    position: absolute;
    left: 209px;
    top: 0;
    width: 311px;
    height: 761px;
    background: var(--paper);
    text-align: center;
    color: var(--ink);
  }
  .brand {
    position: absolute;
    left: 50%;
    top: 405px;
    width: 232px;
    height: 232px;
    margin-left: -116px;
    box-sizing: border-box;
    border: 3px solid var(--ink);
    border-radius: 50%;
    display: flex;
    flex-direction: column;
    align-items: center;
    justify-content: center;
    font-family: "Montserrat", sans-serif;
    font-weight: 500;
    font-size: 36px;
    line-height: 44px;
    letter-spacing: 0.5px;
  }
  .tagline {
    position: absolute;
    left: 0;
    right: 0;
    top: 692px;
    font-family: "Montserrat", sans-serif;
    font-weight: 400;
    font-size: 13px;
    letter-spacing: 0.3px;
  }
  .tagline-sub {
    position: absolute;
    left: 0;
    right: 0;
    top: 717px;
    font-family: "Montserrat", sans-serif;
    font-size: 8px;
    letter-spacing: 0.2px;
  }
  .product-name {
    position: absolute;
    left: 209px;
    top: 810px;
    width: 311px;
    height: 96px;
    background: var(--ink);
    color: var(--paper);
    font-family: "Cabin", sans-serif;
    font-size: 26px;
    line-height: 38px;
    text-align: center;
    display: flex;
    flex-direction: column;
    justify-content: center;
  }
</style>
</head>
<body>
  <main class="bag-front">
    <svg class="loaf-photo" viewBox="0 0 532 900" role="img" aria-label="Photo of a rustic scored sourdough loaf dusted with flour">
      <defs>
        <radialGradient id="crust" cx="45%" cy="45%" r="60%">
          <stop offset="0" stop-color="var(--crust-light)"/>
          <stop offset="0.7" stop-color="var(--crust-mid)"/>
          <stop offset="1" stop-color="var(--crust-dark)"/>
        </radialGradient>
      </defs>
      <ellipse cx="266" cy="450" rx="262" ry="446" fill="url(#crust)"/>
    </svg>
    <div class="wheat-pattern" role="img" aria-label="Repeating pattern of small black wheat sprigs on a diagonal grid across the lower part of the bag"></div>

    <section class="label-band">
      <div class="brand"><span>Dorne's</span><span>Bakery</span></div>
      <div class="tagline">FRASH &amp; DELICIOUS</div>
      <div class="tagline-sub">ALL NATURAL PRODUCT</div>
    </section>

    <div class="product-name"><span>COCONUT</span><span>&amp; RAISIN BREAD</span></div>
  </main>
</body>
</html>
```